Website Design for a High School

School Name: Bayt Nakhla Private Schools
sub-schools:
1-Bayt Nakhla Primary School
2-Bayt Nakhla High School for Girls
3-Bayt Nakhla High School for Boys
The design should be professional and serious and below is the details of the website.
Pages: (Home, About Us, Schools, Events, Students, Gallery, Lectures, Contact Us).
A-) Home Page:
1-Animated photos banner as main
2-Marquee for the last news.
3-Welcoming block of text
4-latest news at the body of the page.
5-Calender "on the side"
6-Number of visitors "on the side"
7-Search bar
8-options to choose a school
B-) School Page:
three schools listed as drop down menu when highlighted over the Schools button in the menu
*Each school page should contain:
1-Student login area
2-Animation photos header
3-Specific news and projects
C-) Student Login page:
have a Report Card
D-) Gallery Page
have a collection of photos.
E-)Contact Page
phone numbers
emails
feedback form
F-)Other mentioned pages
with normal text and photos page look as similar to the Home page.
Required color: Purple as main and include the logo colors
Logo: is attached.
Button link to change language to Arabic.
School
5+ page

```html
<!DOCTYPE html>
<html lang="en">
<head>
<meta charset="utf-8">
<title>Bayt Nakhla Private Schools</title>
<link href="https://fonts.googleapis.com/css2?family=Raleway:wght@300;400;500;600;700&display=swap" rel="stylesheet">
<style>
:root{
  --purple:#6b3f9c;
  --purple-dark:#56297f;
  --purple-soft:rgba(107,63,156,.88);
  --ink:#3a3a3a;
  --muted:#8a8a8a;
  --panel:#f1f1f1;
  --white:#ffffff;
}
*{box-sizing:border-box;margin:0;padding:0}
html,body{width:1200px;height:2348px;overflow:hidden}
body{font-family:'Raleway',sans-serif;color:var(--ink);background:var(--white);position:relative}
.abs{position:absolute}
.hero{left:0;top:0;width:1200px;height:796px;background:linear-gradient(160deg,#7d8a7c 0%,#4c4f5a 45%,#2e2f3a 100%)}
.nav{left:0;top:0;width:1200px;height:62px;background:var(--purple-soft)}
.nav a{position:absolute;top:24px;color:var(--white);font-size:13px;font-weight:600;text-decoration:none;letter-spacing:.3px}
.brand{left:548px;top:0;width:104px;height:104px;border-radius:50%;background:var(--white);border:5px solid var(--purple);display:flex;align-items:center;justify-content:center;text-align:center;color:var(--purple);font-weight:700;font-size:13px;line-height:1.2}
.headline{left:86px;top:360px;color:var(--white)}
.headline h1{font-weight:400;font-size:50px;line-height:1.15;letter-spacing:.5px}
.headline h1 b{font-weight:700}
.headline p{font-size:18px;margin-top:14px;font-weight:500}
.side-panel{left:900px;top:248px;width:214px;height:326px;background:var(--purple-soft);padding:22px 18px;color:var(--white)}
.side-panel h3{font-size:15px;font-weight:500;margin-bottom:6px}
.side-panel p{font-size:12px;line-height:1.4;opacity:.85;margin-bottom:24px}
.side-panel a{color:var(--white);font-size:12px;text-decoration:underline}
.news-band{left:86px;top:595px;width:793px;height:201px;background:rgba(245,245,245,.95)}
.news-tab{left:86px;top:595px;width:71px;height:201px;background:var(--purple);color:var(--white);display:flex;align-items:center;justify-content:center}
.news-tab span{transform:rotate(-90deg);white-space:nowrap;font-size:20px;font-weight:600;letter-spacing:1px}
.item{display:flex;gap:14px;align-items:center}
.date{width:62px;height:58px;border:2px solid var(--purple);color:var(--purple);font-size:13px;font-weight:600;text-align:center;display:flex;flex-direction:column;justify-content:center;line-height:1.3;background:var(--white)}
.date.filled{background:var(--purple);color:var(--white);border:none}
.item h4{font-size:14px;font-weight:500;color:var(--purple);margin-bottom:4px}
.item small{font-size:11px;color:var(--muted)}
.divider{width:1px;background:#d6d6d6}
.video{left:879px;top:595px;width:235px;height:201px;background:linear-gradient(135deg,#c9b7a8,#8f7f94)}
.section-title{font-size:17px;font-weight:700;color:var(--purple);letter-spacing:.3px}
.about-photo{left:94px;top:905px;width:678px;height:259px;background:linear-gradient(120deg,#b79378,#6e7788 60%,#3d4a63)}
.about-side{left:803px;top:910px;width:311px}
.about-side h4{font-size:13px;font-weight:700;color:var(--purple);margin-bottom:10px}
.copy{font-size:12.5px;line-height:1.55;color:var(--muted)}
.gallery{left:86px;top:1357px;width:1028px;display:grid;grid-template-columns:repeat(4,237px);column-gap:27px;row-gap:26px}
.gallery div{height:221px}
.events{left:86px;top:1899px;width:684px;height:345px;background:var(--panel);padding:30px 26px}
.lectures-photo{left:796px;top:1931px;width:318px;height:287px;background:linear-gradient(135deg,#8a9a8c,#3f5a4c 60%,#2d3b36)}
.footer{left:0;top:2288px;width:1200px;height:60px;background:var(--purple);color:var(--white);font-size:13px;display:flex;align-items:center;justify-content:center}
</style>
</head>
<body>
<div class="abs hero" role="img" aria-label="Students in school uniform walking with books on campus"></div>

<nav class="abs nav">
  <a href="#" style="left:86px">HOME</a>
  <a href="#" style="left:155px">ABOUT US</a>
  <a href="#" style="left:250px">SCHOOLS</a>
  <a href="#" style="left:340px">EVENTS</a>
  <a href="#" style="left:750px">STUDENTS</a>
  <a href="#" style="left:848px">GALLERY</a>
  <a href="#" style="left:936px">LECTURES</a>
  <a href="#" style="left:1032px">CONTACT US</a>
</nav>
<div class="abs brand">Bayt<br>Nakhla</div>

<div class="abs headline">
  <h1>AN INNOVATIVE GRADUATE<br><b>SCHOOL</b> OF THEOLOGY</h1>
  <p>Filled with features for a stunning school or university website</p>
</div>

<aside class="abs side-panel">
  <h3>Study with us</h3><p>One of the world's most<br>dynamics capitals</p>
  <h3>Press &amp; media</h3><p>One of the world's most<br>dynamics capitals</p>
  <h3>Departments</h3><p style="margin-bottom:8px">One of the world's most<br>dynamics capitals</p>
  <a href="#">More Services</a>
</aside>

<div class="abs news-band"></div>
<div class="abs news-tab"><span>LATEST NEWS</span></div>
<div class="abs" style="left:188px;top:622px;display:flex;gap:36px">
  <div style="display:flex;flex-direction:column;gap:22px;width:310px">
    <div class="item"><div class="date">15 May<br>2015</div><div><h4>Bayt Nakhla Primary School</h4><small>When: 15 May 2016 @ 7:00 am</small></div></div>
    <div class="item"><div class="date">15 May<br>2015</div><div><h4>Bayt Nakhla High School for Girls</h4><small>When: 15 May 2016 @ 7:00 am</small></div></div>
  </div>
  <div class="divider" style="height:140px"></div>
  <div style="display:flex;flex-direction:column;gap:22px">
    <div class="item"><div class="date">15 May<br>2015</div><div><h4>Bayt Nakhla High School for Boys</h4><small>When: 15 May 2016 @ 7:00 am</small></div></div>
    <div class="item"><div class="date">15 May<br>2015</div><div><h4>Bayt Nakhla Primary School</h4><small>When: 15 May 2016 @ 7:00 am</small></div></div>
  </div>
</div>
<div class="abs video" role="img" aria-label="Video still of students in a classroom"></div>
<svg class="abs" style="left:966px;top:665px" width="60" height="60" viewBox="0 0 60 60"><circle cx="30" cy="30" r="28" fill="none" stroke="#fff" stroke-width="3"/><path d="M24 19 L42 30 L24 41 Z" fill="#fff"/></svg>

<h2 class="abs section-title" style="left:86px;top:864px">ABOUT US</h2>
<div class="abs about-photo" role="img" aria-label="Group of smiling primary school pupils"></div>
<div class="abs about-side">
  <h4>BAYT NAKHLA PRIMARY SCHOOL</h4>
  <p class="copy">Lorem ipsum dolor sit amet, consectetuer adipiscing elit, sed diam nonummy nibh euismod tincidunt ut laoreet dolore magna aliquam erat volutpat. Ut wisi enim ad minim veniam, quis nostrud exerci tation ullamcorper suscipit lobortis nisl ut aliquip ex ea commodo consequat. Duis autem vel eum iriure dolor in hendrerit in vulputate velit esse molestie consequat, vel illum dolore eu feugiat nulla facilisis at vero eros et accumsan et iusto odio dignissim qui blandit praesent luptatum zzril delenit augue duis dolore te feugait nulla facilisi.</p>
</div>
<p class="abs copy" style="left:86px;top:1182px;width:1028px">Lorem ipsum dolor sit amet, consectetuer adipiscing elit, sed diam nonummy nibh euismod tincidunt ut laoreet dolore magna aliquam erat volutpat. Ut wisi enim ad minim veniam, quis nostrud exerci tation ullamcorper suscipit lobortis nisl ut aliquip ex ea commodo consequat. Duis autem vel eum iriure dolor in hendrerit in vulputate velit esse molestie consequat, vel illum dolore eu feugiat nulla. Nam liber tempor cum soluta nobis eleifend option congue nihil imperdiet doming id quod mazim placerat facer possim assum.</p>

<h2 class="abs section-title" style="left:86px;top:1323px">SCHOOL/GALLERY</h2>
<div class="abs gallery">
  <div role="img" aria-label="Red brick school building" style="background:linear-gradient(#a9c4df,#8a4b3c 55%,#6f7a5a)"></div>
  <div role="img" aria-label="School building with clock tower" style="background:linear-gradient(#9fc1e6,#a0583f 55%,#7a6d60)"></div>
  <div role="img" aria-label="Modern school entrance with green roof" style="background:linear-gradient(#b7d3ea,#4d8a7a 35%,#b7856a 70%,#7b7b70)"></div>
  <div role="img" aria-label="Curved modern school building" style="background:linear-gradient(#5d9fe0,#d9d3cc 50%,#a55f4a 75%,#8f8f8f)"></div>
  <div role="img" aria-label="Group of students smiling" style="background:linear-gradient(135deg,#8f5a3e,#c23b3b 55%,#3b3b4a)"></div>
  <div role="img" aria-label="Students reading a book together" style="background:linear-gradient(135deg,#c9a98d,#e7e2dd 55%,#5a5a70)"></div>
  <div role="img" aria-label="Two students holding folders" style="background:linear-gradient(135deg,#d8c0a0,#3f5a3a 55%,#2c2c2c)"></div>
  <div role="img" aria-label="Student studying at a laptop" style="background:linear-gradient(135deg,#efe9e4,#d8718a 55%,#c8c0bb)"></div>
</div>

<section class="abs events">
  <h2 class="section-title" style="margin-bottom:26px">LATEST EVENTS</h2>
  <div style="display:flex;gap:30px">
    <div style="display:flex;flex-direction:column;gap:26px;width:300px">
      <div class="item"><div class="date filled">15 May<br>2015</div><div><h4>Bayt Nakhla Primary School</h4><small>When: 15 May 2016 @ 7:00 am</small></div></div>
      <div class="item"><div class="date filled">15 May<br>2015</div><div><h4>Bayt Nakhla High School for Girls</h4><small>When: 15 May 2016 @ 7:00 am</small></div></div>
    </div>
    <div class="divider" style="height:150px"></div>
    <div style="display:flex;flex-direction:column;gap:26px">
      <div class="item"><div class="date filled">15 May<br>2015</div><div><h4>Bayt Nakhla High School for Boys</h4><small>When: 15 May 2016 @ 7:00 am</small></div></div>
      <div class="item"><div class="date filled">15 May<br>2015</div><div><h4>Bayt Nakhla Primary School</h4><small>When: 15 May 2016 @ 7:00 am</small></div></div>
    </div>
  </div>
</section>

<h2 class="abs section-title" style="left:796px;top:1895px">LECTURES</h2>
<div class="abs lectures-photo" role="img" aria-label="Teacher with students in front of a chalkboard"></div>

<footer class="abs footer">Copyright © 2015 Bayt Nakhla Private Schools. All Reserved</footer>
</body>
</html>
```